Supplement Bottle Packaging and Design

We want to rebrand our current health supplements (see below). We do want it to be modern, vibrant and appealing supplement bottles. Very upscale and elegant as it targets primarily women.
NOTE: READ THE ATTACHED WORD DOCUMENT!
Bottle size: We are totally open to the bottle size and shape, as long it's a typical supplement bottle size to handle 90-120 capsules; what we mostly need is new bottle design/packaging. YOU DON’T HAVE TO USE THE CURRENT WHITE BOTTLE SHAPE, BUT ANYTHING MORE MODERN WOULD WORK!
Updates
We need more modern, clean sleek designs to choose from
Look and feel
Each slider illustrates characteristics of the customer's brand and the style your logo design should communicate.

```html
<!DOCTYPE html>
<html lang="en">
<head>
<meta charset="utf-8">
<title>Luma Clear – Supplement Label</title>
<link rel="stylesheet" href="https://fonts.googleapis.com/css2?family=Montserrat:wght@500;600;700&family=Roboto+Condensed:wght@400;500;600&display=swap">
<style>
  :root {
    --backdrop: #fdd3d2;
    --label-white: #f3f3f3;
    --purple-deep: #4e1572;
    --purple-mid: #7a3a9e;
    --purple-soft: #a070c0;
    --text-grey: #6a6a6a;
    --text-dark: #444444;
    --white: #ffffff;
  }
  * { box-sizing: border-box; margin: 0; padding: 0; }
  html, body {
    width: 1136px;
    height: 1200px;
    overflow: hidden;
    background: var(--backdrop);
  }
  .canvas {
    position: relative;
    width: 1136px;
    height: 1200px;
  }
  .label {
    position: absolute;
    left: 328px;
    top: 369px;
    width: 485px;
    height: 633px;
    background: var(--label-white);
    overflow: hidden;
  }
  .label__hero {
    position: absolute;
    left: 0;
    top: 0;
    width: 444px;
    height: 409px;
    border-bottom-right-radius: 36px;
    overflow: hidden;
  }
  .label__hero-art {
    position: absolute;
    inset: 0;
    background: linear-gradient(135deg, var(--purple-soft) 0%, var(--purple-mid) 45%, var(--purple-deep) 100%);
  }
  .product-name {
    position: absolute;
    left: 72px;
    top: 168px;
    font-family: "Montserrat", sans-serif;
    font-weight: 600;
    font-size: 102px;
    line-height: 116px;
    letter-spacing: -3px;
    color: var(--white);
    white-space: nowrap;
  }
  .tagline {
    position: absolute;
    left: 0;
    right: 0;
    top: 434px;
    text-align: center;
    font-family: "Montserrat", sans-serif;
    font-size: 16.5px;
    font-weight: 600;
    color: var(--text-grey);
    letter-spacing: 0.2px;
  }
  .tagline strong { color: var(--text-dark); font-weight: 700; }
  .count {
    position: absolute;
    left: 72px;
    top: 520px;
    font-family: "Roboto Condensed", sans-serif;
    color: var(--purple-deep);
    text-align: center;
  }
  .count__number {
    display: block;
    font-size: 40px;
    line-height: 38px;
    font-weight: 400;
    letter-spacing: -1px;
  }
  .count__unit {
    display: block;
    font-size: 12.5px;
    line-height: 14px;
    font-weight: 500;
  }
  .supplement-pill {
    position: absolute;
    left: 142px;
    right: 0;
    top: 521px;
    height: 72px;
    border-radius: 22px 0 0 22px;
    background: linear-gradient(90deg, var(--purple-mid) 0%, var(--purple-deep) 50%, var(--purple-mid) 100%);
    display: flex;
    align-items: center;
    padding-left: 22px;
    font-family: "Roboto Condensed", sans-serif;
    font-size: 30px;
    color: var(--white);
    letter-spacing: -0.5px;
  }
  .supplement-pill strong { font-weight: 600; margin-right: 7px; }
</style>
</head>
<body>
<main class="canvas">
  <section class="label">
    <div class="label__hero">
      <div class="label__hero-art" role="img" aria-label="Purple tropical leaf pattern background"></div>
      <h1 class="product-name">LUMA<br>CLEAR</h1>
    </div>
    <p class="tagline">Rejuvenating <strong>Cleanse &amp; Detox Formula</strong>*</p>
    <div class="count">
      <span class="count__number">120</span>
      <span class="count__unit">VEGETABLE<br>CAPSULES</span>
    </div>
    <div class="supplement-pill"><strong>DIETARY</strong> SUPPLEMENT</div>
  </section>
</main>
</body>
</html>
```